Meridel Hair Studio Needs a new appointment business card

We need a new appointment card for our hair salon.

I Dont want bright out there colours.
I would like it to be neat, clean, easy to read. White, Black, with a hint of colour if needed.

We need
-Logo
-Phone number 47208613
-Mobile Number: 0417306852
Address: Shop 3/214 Calder Road, The Elmgates, Torrindale 4812

BACK SIDE OF CARD
- Appointment Time & Date (White background so we are able to write on it)
(If you are unable to make your appointment please contact us ASAP 47208613)

I also would like the chatterly and Pictorama logo(Find us on Chatterly)(find us on Pictorama)

Target Market(s)

appointment card simple to read. all information for their next appoint For all our clients male and female

Industry/Entity Type

Hairdresser

Contact Information for Business Card

-Logo
-Phone number 47208613

BACK SIDE OF CARD

Font styles to use
Serif
Sans Serif
Script

Requirements
Must have
• White Back ground on backside with appointment deatils so we are able to write information (like appointment time and date)
Nice to have
• Find us on Chatterly
and
pictorama - meridel_hairstudio
Should not have
• BRIGHT COLOURS

```html
<!DOCTYPE html>
<html lang="en">
<head>
<meta charset="utf-8">
<title>Meridel Hair Studio – Appointment Card</title>
<link rel="stylesheet" href="https://fonts.googleapis.com/css2?family=Arimo&family=Montserrat:wght@400;500;600&display=swap">
<style>
  :root {
    --ink: #111111;
    --paper: #ffffff;
    --rule: #333333;
    --faint: #d9d9d9;
    --card-border: #555555;
  }
  * { margin: 0; padding: 0; box-sizing: border-box; }
  html, body { width: 1200px; height: 622px; overflow: hidden; background: var(--paper); }
  .sheet { position: relative; width: 1200px; height: 622px; color: var(--ink); font-family: "Montserrat", sans-serif; }
  .band { position: absolute; left: 0; width: 100%; background: var(--ink); }
  .band--top { top: 0; height: 14px; }
  .band--bottom { bottom: 0; height: 13px; }

  .heading { position: absolute; left: 0; width: 100%; text-align: center; font-family: "Arimo", sans-serif; font-size: 19.5px; line-height: 24.5px; }
  .heading--title { top: 43px; }
  .heading--option { top: 152px; font-size: 17.5px; }

  .card { position: absolute; top: 234px; width: 468px; height: 267px; border: 1px solid var(--card-border); background: var(--paper); overflow: hidden; }
  .card--front { left: 116px; }
  .card--back { left: 613px; }

  .brand { position: absolute; left: 30px; top: 52px; display: flex; align-items: center; gap: 8px; }
  .brand__name { font-weight: 600; font-size: 17px; letter-spacing: 0.6px; color: var(--ink); }
  .brand__dot { width: 12px; height: 12px; border-radius: 50%; background: var(--ink); }

  .contact { position: absolute; left: 34px; font-size: 14px; line-height: 18px; display: flex; align-items: flex-start; gap: 8px; }
  .contact svg { flex: none; width: 14px; height: 16px; margin-top: 1px; }
  .contact--phone { top: 129px; }
  .contact--mobile { top: 160px; }
  .contact--address { top: 191px; }

  .front-art { position: absolute; right: 0; top: 0; width: 236px; height: 267px;
    background: linear-gradient(135deg, rgba(17,17,17,0.15) 20%, rgba(17,17,17,0.8) 100%);
    clip-path: polygon(58% 0, 100% 0, 100% 100%, 58% 100%, 70% 60%, 40% 100%, 20% 100%); }
  .back-art { position: absolute; left: 0; bottom: 0; width: 135px; height: 145px; background: linear-gradient(45deg, var(--faint) 0%, rgba(217,217,217,0) 80%); }

  .back-title { position: absolute; top: 27px; left: 0; width: 100%; text-align: center; font-size: 16px; font-weight: 500; letter-spacing: 0.3px; }
  .field { position: absolute; top: 65px; display: flex; align-items: flex-end; font-size: 14px; font-weight: 500; }
  .field__line { display: block; height: 1px; background: var(--rule); margin-left: 4px; margin-bottom: 3px; }
  .field--date { left: 32px; }
  .field--date .field__line { width: 158px; }
  .field--time { left: 238px; }
  .field--time .field__line { width: 158px; }
  .notice { position: absolute; top: 91px; left: 0; width: 100%; text-align: center; font-size: 13.5px; line-height: 18px; }

  .social-title { position: absolute; top: 182px; left: 0; width: 100%; text-align: center; font-size: 16px; font-weight: 500; }
  .social { position: absolute; left: 0; width: 100%; display: flex; justify-content: center; align-items: center; gap: 5px; font-size: 14px; }
  .social--chatterly { top: 206px; }
  .social--pictorama { top: 229px; }
  .social__label { font-weight: 500; }
  .social__mark-square { width: 12px; height: 12px; background: var(--ink); border-radius: 2px; }
  .social__mark-circle { width: 12px; height: 12px; background: var(--ink); border-radius: 50%; }
</style>
</head>
<body>
<main class="sheet">
  <div class="band band--top"></div>

  <p class="heading heading--title">Meridel Hair Studio<br>Logo Design</p>
  <p class="heading heading--option">Option 1</p>

  <section class="card card--front" aria-label="Card front">
    <div class="front-art" role="img" aria-label="Large open scissors decoration"></div>
    <div class="brand">
      <span class="brand__name">MERIDEL HAIR STUDIO</span>
      <span class="brand__dot"></span>
    </div>
    <p class="contact contact--phone">
      <svg viewBox="0 0 16 16" aria-hidden="true"><path fill="currentColor" d="M2 6c0-2 2-3 6-3s6 1 6 3v1h-3V6H5v1H2zM4 8h8l2 5H2zM6 9v2h4V9z"/></svg>
      <span>47208613</span>
    </p>
    <p class="contact contact--mobile">
      <svg viewBox="0 0 16 16" aria-hidden="true"><rect x="4" y="1" width="8" height="14" rx="1.5" fill="none" stroke="currentColor" stroke-width="1.6"/><line x1="7" y1="12.5" x2="9" y2="12.5" stroke="currentColor" stroke-width="1.4"/></svg>
      <span>0417306852</span>
    </p>
    <p class="contact contact--address">
      <svg viewBox="0 0 16 16" aria-hidden="true"><path fill="currentColor" d="M8 1a5 5 0 0 1 5 5c0 4-5 9-5 9S3 10 3 6a5 5 0 0 1 5-5zm0 3a2 2 0 1 0 0 4 2 2 0 0 0 0-4z"/></svg>
      <span>Shop 3/214 Calder Road, The<br>Elmgates, Torrindale 4812</span>
    </p>
  </section>

  <section class="card card--back" aria-label="Card back">
    <div class="back-art" role="img" aria-label="Faint scissors decoration"></div>
    <h2 class="back-title">Appointment Details</h2>
    <p class="field field--date">Date<span class="field__line"></span></p>
    <p class="field field--time">Time<span class="field__line"></span></p>
    <p class="notice">If you are unable to make your appointment<br>please contact us ASAP 47208613</p>
    <h3 class="social-title">Find us on Social Media</h3>
    <p class="social social--chatterly"><span class="social__mark-square"></span><span class="social__label">Chatterly</span> meridelhairstudioelmgates</p>
    <p class="social social--pictorama"><span class="social__mark-circle"></span><span class="social__label">Pictorama</span> meridel_hairstudio</p>
  </section>

  <div class="band band--bottom"></div>
</main>
</body>
</html>
```